Letterhead design for VELMORA company

I need an A4 letterhead design for my company "Velmora Household Wares". I need the letterhead to match my current logo and business card designs. I would like it to be colourful and match the design of the business card in terms of the flowing line of colour where the information is.  

Target Market(s)

Adults aged 20 - 50 Upper middle class.

Industry/Entity Type

It Company

Requirements
Must have
• Must be A4 size and match my current logo and business card designs. Must be clean simple and eye catching.

• Must have the following information

• Velmora Household Wares LTD
• 7 Harbeck Row
• Chiswick
• London
• England
• W7 2RZ
• Company No. 04521963
• VAT No. GB 371562048

• Telephone: 02079460318
• Mobile: 07700900412
• Email: info@velmora-wares.co.uk
Nice to have
• nice to have a wave of colour like the business card.
Should not have
• Should not be a different colour scheme to the business card and logo design.

```html
<!DOCTYPE html>
<html lang="en">
<head>
<meta charset="utf-8">
<title>Velmora Household Wares – Letterhead</title>
<link rel="stylesheet" href="https://fonts.googleapis.com/css2?family=PT+Sans:wght@400&display=swap">
<style>
  :root {
    --teal-deep: #178e9c;
    --teal: #2fb8c0;
    --teal-bright: #6ff5ec;
    --silver: #dcdcdc;
    --label: #1db7c0;
    --navy: #2b4b8f;
    --ink: #111111;
    --edge: #444444;
    --paper: #ffffff;
  }
  html, body {
    margin: 0;
    padding: 0;
    width: 848px;
    height: 1200px;
    overflow: hidden;
    background: var(--paper);
    font-family: "PT Sans", "Myriad Pro", Arial, sans-serif;
  }
  .letterhead {
    position: relative;
    width: 848px;
    height: 1200px;
    overflow: hidden;
  }
  .sheet {
    position: absolute;
    left: 14px;
    top: 24px;
    width: 822px;
    height: 1163px;
    border-top: 1px solid #9a9a9a;
    border-left: 1px solid #9a9a9a;
    border-right: 3px solid var(--edge);
    border-bottom: 3px solid var(--edge);
    box-sizing: border-box;
  }
  .header-band {
    position: absolute;
    left: 244px;
    top: 25px;
    width: 589px;
    height: 86px;
    background: linear-gradient(180deg, #f4f4f4 0%, var(--silver) 45%, var(--teal-bright) 75%, var(--teal) 100%);
  }
  .brand {
    position: absolute;
    left: 46px;
    top: 72px;
  }
  .brand-name {
    margin: 0;
    font-size: 46px;
    line-height: 1;
    letter-spacing: 1px;
    color: var(--teal-deep);
    font-weight: 400;
  }
  .brand-tagline {
    margin: 4px 0 0 1px;
    font-size: 18px;
    line-height: 1;
    letter-spacing: 1.8px;
    color: var(--navy);
  }
  .address {
    position: absolute;
    left: 47px;
    top: 150px;
    margin: 0;
    font-style: normal;
    font-size: 16.5px;
    line-height: 19.7px;
    color: var(--ink);
  }
  .details {
    position: absolute;
    left: 583px;
    top: 144px;
    margin: 0;
    padding: 0;
    list-style: none;
    font-size: 16.5px;
    color: var(--ink);
    white-space: nowrap;
  }
  .details li { height: 21.5px; line-height: 21.5px; }
  .details .label { color: var(--label); }
</style>
</head>
<body>
<main class="letterhead">
  <div class="sheet"></div>

  <div class="header-band" role="img" aria-label="Flowing teal and silver wave of colour across the top of the page"></div>

  <header class="brand">
    <h1 class="brand-name">VELMORA</h1>
    <p class="brand-tagline">Household Wares</p>
  </header>

  <address class="address">
    Velmora Household Wares LTD<br>
    7 Harbeck Row<br>
    Chiswick<br>
    London<br>
    England<br>
    W7 2RZ
  </address>

  <ul class="details">
    <li><span class="label">Company No.</span> 04521963</li>
    <li><span class="label">VAT No.</span> GB 371562048</li>
    <li><span class="label">Telephone:</span> 02079460318</li>
    <li><span class="label">Mobile:</span> 07700900412</li>
    <li><span class="label">Email:</span> info@velmora-wares.co.uk</li>
  </ul>
</main>
</body>
</html>
```